Quality Improvement Software for healthcare agencies needs a website.

Veltrix820 is a software for hospices and home health agencies to manage their Quality Assurance Performance Improvement programs to remain complaint with the standards set by Sanovia and the Bureau of Civic Wellbeing. The web accessible software-as-a-service provides an easy, turn-key way for agencies to organize all the information they need to manage and track.

Coded - Design and coding required

4 page

```html
<!DOCTYPE html>
<html lang="en">
<head>
<meta charset="utf-8">
<title>Veltrix820 — Quality Assurance Performance Improvement</title>
<link rel="stylesheet" href="https://fonts.googleapis.com/css2?family=Montserrat:wght@500;600;700&family=Nunito+Sans:wght@400;600;700&display=swap">
<style>
:root{
  --navy:#1b2b49;
  --navy-deep:#16243f;
  --title-blue:#1f4c8f;
  --orange:#f7931e;
  --green:#7cc242;
  --sky:#29a8e0;
  --yellow:#f6c924;
  --text:#3d4552;
  --muted:#d9dde4;
  --white:#ffffff;
}
*{box-sizing:border-box;margin:0;padding:0}
html,body{width:1200px;height:3520px;overflow:hidden;background:var(--white)}
body{position:relative;font-family:"Nunito Sans",sans-serif;color:var(--text)}
.abs{position:absolute}

/* header */
.site-header{position:absolute;left:0;top:0;width:1200px;height:94px;background:var(--white)}
.brand{position:absolute;display:flex;align-items:center;gap:10px;font-family:"Montserrat",sans-serif;font-weight:600;color:var(--navy)}
.brand-mark{width:22px;height:22px;background:var(--orange)}
.site-header .brand{left:111px;top:28px;font-size:32px}
.nav{position:absolute;top:37px;left:528px;display:flex;gap:0;font-family:"Montserrat",sans-serif;font-size:15px;color:#4b5260}
.nav a{text-decoration:none;color:inherit;position:absolute;white-space:nowrap}
.nav .active{font-weight:600;color:var(--navy)}
.btn{display:inline-block;background:var(--orange);color:var(--white);font-family:"Montserrat",sans-serif;font-weight:600;font-size:15px;border-radius:4px;text-align:center;text-decoration:none}
.header-quote{position:absolute;left:936px;top:27px;width:152px;height:40px;line-height:40px}

/* hero */
.hero{position:absolute;left:0;top:94px;width:1200px;height:514px;background:linear-gradient(90deg,#cfb79a,#e8d3bd 45%,#b9c7cf)}
.hero-overlay{position:absolute;left:22px;top:18px;width:1156px;height:478px;background:linear-gradient(100deg,rgba(247,166,80,.85) 0%,rgba(240,190,120,.55) 35%,rgba(70,185,200,.7) 65%,rgba(135,200,80,.8) 100%)}
.hero h1{position:absolute;left:0;top:305px;width:1200px;text-align:center;font-family:"Montserrat",sans-serif;font-weight:700;font-size:44px;line-height:56px;color:var(--white);text-transform:uppercase}
.scroll-cue{position:absolute;left:583px;top:432px}

/* section headings */
.section-title{position:absolute;left:0;width:1200px;display:flex;justify-content:center;align-items:center;gap:16px;font-family:"Montserrat",sans-serif;font-weight:700;font-size:40px;color:var(--navy)}
.section-title .brand-mark{width:24px;height:24px}

/* about */
.about-photo{position:absolute;left:111px;top:767px;width:545px;height:535px;padding:3px;background:linear-gradient(160deg,var(--orange),var(--sky) 40%,var(--yellow) 75%,var(--green))}
.about-photo .fill{width:100%;height:100%;background:linear-gradient(135deg,#6f7f77,#d8d9d6 50%,#eef0f2)}
.about-card{position:absolute;left:580px;top:833px;width:506px;height:402px;background:var(--navy);border:4px solid var(--white);box-shadow:0 6px 20px rgba(0,0,0,.15);padding:32px 26px 0 28px;color:var(--white);font-size:15.5px;line-height:31px}
.about-card p+p{margin-top:14px}
.about-card .btn{margin-top:22px;width:152px;height:40px;line-height:40px}

/* services */
.service{position:absolute;width:477px;height:252px;border:3px solid;border-bottom-color:var(--navy);padding:26px 22px 0 22px}
.service h3{display:flex;align-items:center;gap:18px;font-family:"Montserrat",sans-serif;font-weight:600;font-size:21px;color:var(--title-blue);height:46px}
.service-icon{width:56px;height:46px;flex:none}
.service p{margin-top:12px;font-size:15.5px;line-height:28.5px;color:var(--text)}
.s-blue{border-top-color:var(--sky);border-left-color:var(--sky);border-right-color:var(--sky)}
.s-green{border-top-color:var(--green);border-left-color:var(--green);border-right-color:var(--green)}
.s-orange{border-top-color:var(--orange);border-left-color:var(--orange);border-right-color:var(--orange)}
.s-yellow{border-top-color:var(--yellow);border-left-color:var(--yellow);border-right-color:var(--yellow)}

/* blog */
.blog-photo{position:absolute;top:2266px;width:311px;height:205px}
.blog-text{position:absolute;top:2450px;width:292px;height:136px;background:var(--white);box-shadow:0 4px 18px rgba(0,0,0,.1);text-align:center;padding-top:32px}
.blog-text h4{font-family:"Montserrat",sans-serif;font-weight:600;font-size:15px;color:var(--navy)}
.blog-text p{margin-top:12px;font-size:14px;line-height:22px;color:#555c68}
.blog-text.featured{background:linear-gradient(80deg,var(--navy) 5%,var(--sky) 40%,var(--green) 65%,var(--orange) 90%)}
.blog-text.featured h4,.blog-text.featured p{color:var(--white)}

/* faq */
.faq-item{position:absolute;left:111px;width:977px;height:66px;border:2px solid var(--muted);display:flex;align-items:center;padding-left:20px;font-size:17px;color:var(--text)}
.faq-item svg.arrow{margin-right:16px}
.faq-toggle{position:absolute;right:30px;top:12px;width:42px;height:38px;background:var(--title-blue);border-radius:3px;display:flex;align-items:center;justify-content:center;background:linear-gradient(180deg,#1f4c8f,#17305c)}

/* footer */
.site-footer{position:absolute;left:0;top:3254px;width:1200px;height:266px;background:var(--navy);color:var(--white)}
.site-footer .brand{left:111px;top:80px;font-size:40px;color:var(--white)}
.copyright{position:absolute;left:111px;top:152px;font-size:17px;line-height:28px}
.footer-col{position:absolute;top:62px;font-size:17px;line-height:28px}
.footer-col h5{font-family:"Nunito Sans",sans-serif;font-weight:600;font-size:17px;margin-bottom:16px;text-transform:uppercase}
.contact-line{position:relative;padding-left:28px}
.contact-line svg{position:absolute;left:0;top:6px}
</style>
</head>
<body>

<header class="site-header">
  <div class="brand"><span class="brand-mark"></span>Veltrix820</div>
  <nav class="nav">
    <a class="active" style="left:0">Home</a>
    <a style="left:76px">About</a>
    <a style="left:152px">Services</a>
    <a style="left:243px">Blog</a>
    <a style="left:308px">Contact</a>
  </nav>
  <a class="btn header-quote">Request Quote</a>
</header>

<section class="hero" role="img" aria-label="Photo of a nurse caring for a smiling elderly woman at home">
  <div class="hero-overlay"></div>
  <h1>Quality Assurance Performance<br>Improvement Programs</h1>
  <svg class="scroll-cue" width="34" height="36" viewBox="0 0 34 36">
    <circle cx="17" cy="18" r="16" fill="#1aa3c9" opacity=".8"/>
    <rect x="11" y="7" width="12" height="20" rx="6" fill="none" stroke="#fff" stroke-width="2"/>
    <path d="M17 11v8M14 16l3 3 3-3" stroke="#fff" stroke-width="1.8" fill="none"/>
  </svg>
</section>

<h2 class="section-title" style="top:676px"><span class="brand-mark"></span>ABOUT US</h2>

<div class="about-photo"><div class="fill" role="img" aria-label="Photo of a smiling doctor working on a laptop"></div></div>
<div class="about-card">
  <p>Lorem ipsum dolor sit amet, consectetur adipiscing elit, sed do eiusmod tempor incididunt ut labore et dolore magna aliqua. Ut enim ad minim veniam, quis nostrud exercitation ullamco laboris nisi ut aliquip ex ea commodo consequat.</p>
  <p>Duis aute irure dolor in reprehenderit in voluptate velit esse cillum dolore eu fugiat nulla pariatur. Excepteur sint occae cat cupidatat non proident, sunt in culpa qui officia deserunt mollit anim id est laborum.</p>
  <a class="btn">Request Quote</a>
</div>

<h2 class="section-title" style="top:1414px"><span class="brand-mark"></span>OUR SERVICES</h2>

<article class="service s-blue" style="left:111px;top:1519px">
  <h3><svg class="service-icon" viewBox="0 0 56 46"><circle cx="34" cy="23" r="20" fill="#cde9f7"/><rect x="6" y="8" width="30" height="30" rx="2" fill="none" stroke="#1b2b49" stroke-width="2"/><path d="M12 16h18M12 23h18M12 30h12" stroke="#1b2b49" stroke-width="2"/></svg>Electronic Health Records</h3>
  <p>Lorem ipsum dolor sit amet, consectetur adipiscing elit, sed do eiusmod tempor incididunt ut labore et dolore magna aliqua. Ut enim ad minim veniam, quis nostrud exercitation ullamco laboris nisi ut aliquip ex ea commodo consequat.</p>
</article>
<article class="service s-green" style="left:611px;top:1519px">
  <h3><svg class="service-icon" viewBox="0 0 56 46"><circle cx="34" cy="23" r="20" fill="#dcefc9"/><circle cx="24" cy="17" r="10" fill="none" stroke="#1b2b49" stroke-width="2"/><path d="M19 17l4 4 6-7" stroke="#1b2b49" stroke-width="2" fill="none"/></svg>Quality Assurance</h3>
  <p>Lorem ipsum dolor sit amet, consectetur adipiscing elit, sed do eiusmod tempor incididunt ut labore et dolore magna aliqua. Ut enim ad minim veniam, quis nostrud exercitation ullamco laboris nisi ut aliquip ex ea commodo consequat.</p>
</article>
<article class="service s-orange" style="left:111px;top:1795px">
  <h3><svg class="service-icon" viewBox="0 0 56 46"><circle cx="34" cy="23" r="20" fill="#fde0bd"/><rect x="6" y="6" width="32" height="26" rx="2" fill="none" stroke="#1b2b49" stroke-width="2"/><path d="M6 13h32" stroke="#1b2b49" stroke-width="2"/><circle cx="14" cy="35" r="6" fill="#fff" stroke="#1b2b49" stroke-width="2"/></svg>Manage and Track</h3>
  <p>Lorem ipsum dolor sit amet, consectetur adipiscing elit, sed do eiusmod tempor incididunt ut labore et dolore magna aliqua. Ut enim ad minim veniam, quis nostrud exercitation ullamco laboris nisi ut aliquip ex ea commodo consequat.</p>
</article>
<article class="service s-yellow" style="left:611px;top:1795px">
  <h3><svg class="service-icon" viewBox="0 0 56 46"><circle cx="34" cy="23" r="20" fill="#fdf0b8"/><rect x="8" y="12" width="26" height="26" rx="2" fill="none" stroke="#1b2b49" stroke-width="2"/><path d="M13 12V7h22v26h-1" stroke="#1b2b49" stroke-width="2" fill="none"/></svg>Organize Information</h3>
  <p>Lorem ipsum dolor sit amet, consectetur adipiscing elit, sed do eiusmod tempor incididunt ut labore et dolore magna aliqua. Ut enim ad minim veniam, quis nostrud exercitation ullamco laboris nisi ut aliquip ex ea commodo consequat.</p>
</article>

<h2 class="section-title" style="top:2170px"><span class="brand-mark"></span>LATEST BLOG</h2>

<div class="blog-photo" style="left:111px;background:linear-gradient(135deg,#c9ccd0,#eef0f2 60%,#9aa2a8)" role="img" aria-label="Photo of doctors reviewing a tablet together"></div>
<div class="blog-photo" style="left:444px;background:linear-gradient(135deg,#12394d,#2f7894 50%,#0f2a38)" role="img" aria-label="Photo of a clinician studying scans on monitors"></div>
<div class="blog-photo" style="left:777px;background:linear-gradient(135deg,#dfe3e6,#f3f4f5 50%,#7d97b3)" role="img" aria-label="Photo of a doctor reading a tablet in a hospital corridor"></div>

<div class="blog-text" style="left:120px"><h4>NEMO ENIM IPSAM OLUPTAS</h4><p>Sed ut perspiciatis unde omnis iste sit<br>voluptatem.accusaium doloremq.</p></div>
<div class="blog-text" style="left:453px"><h4>NEMO ENIM IPSAM OLUPTAS</h4><p>Sed ut perspiciatis unde omnis iste sit<br>voluptatem.accusaium doloremq.</p></div>
<div class="blog-text featured" style="left:786px"><h4>NEMO ENIM IPSAM OLUPTAS</h4><p>Sed ut perspiciatis unde omnis iste<br>sit voluptatem.accusaium doloremq.</p></div>

<h2 class="section-title" style="top:2694px"><span class="brand-mark"></span>FREQUENTLY ASKED QUESTIONS</h2>

<div class="faq-item" style="top:2788px"><svg class="arrow" width="20" height="16" viewBox="0 0 20 16"><path d="M1 8h17M11 1l7 7-7 7" stroke="#1b2b49" stroke-width="2" fill="none"/></svg>Ut enim ad minima veniam, quis nostrum exercitationem ullam corporis suscipit?<span class="faq-toggle"><svg width="16" height="10" viewBox="0 0 16 10"><path d="M2 2l6 6 6-6" stroke="#fff" stroke-width="2.4" fill="none"/></svg></span></div>
<div class="faq-item" style="top:2876px"><svg class="arrow" width="20" height="16" viewBox="0 0 20 16"><path d="M1 8h17M11 1l7 7-7 7" stroke="#1b2b49" stroke-width="2" fill="none"/></svg>Ut enim ad minima veniam, quis nostrum exercitationem ullam corporis suscipit?<span class="faq-toggle"><svg width="16" height="10" viewBox="0 0 16 10"><path d="M2 2l6 6 6-6" stroke="#fff" stroke-width="2.4" fill="none"/></svg></span></div>
<div class="faq-item" style="top:2964px"><svg class="arrow" width="20" height="16" viewBox="0 0 20 16"><path d="M1 8h17M11 1l7 7-7 7" stroke="#1b2b49" stroke-width="2" fill="none"/></svg>Ut enim ad minima veniam, quis nostrum exercitationem ullam corporis suscipit?<span class="faq-toggle"><svg width="16" height="10" viewBox="0 0 16 10"><path d="M2 2l6 6 6-6" stroke="#fff" stroke-width="2.4" fill="none"/></svg></span></div>
<div class="faq-item" style="top:3052px"><svg class="arrow" width="20" height="16" viewBox="0 0 20 16"><path d="M1 8h17M11 1l7 7-7 7" stroke="#1b2b49" stroke-width="2" fill="none"/></svg>Ut enim ad minima veniam, quis nostrum exercitationem ullam corporis suscipit?<span class="faq-toggle"><svg width="16" height="10" viewBox="0 0 16 10"><path d="M2 2l6 6 6-6" stroke="#fff" stroke-width="2.4" fill="none"/></svg></span></div>
<div class="faq-item" style="top:3140px"><svg class="arrow" width="20" height="16" viewBox="0 0 20 16"><path d="M1 8h17M11 1l7 7-7 7" stroke="#1b2b49" stroke-width="2" fill="none"/></svg>Ut enim ad minima veniam, quis nostrum exercitationem ullam corporis suscipit?<span class="faq-toggle"><svg width="16" height="10" viewBox="0 0 16 10"><path d="M2 2l6 6 6-6" stroke="#fff" stroke-width="2.4" fill="none"/></svg></span></div>

<footer class="site-footer">
  <div class="brand"><span class="brand-mark" style="width:26px;height:26px"></span>Veltrix820</div>
  <div class="copyright">2023 Veltrix820.<br>All Rights Reserved.</div>
  <div class="footer-col" style="left:442px">
    <h5>Contact Us</h5>
    <div class="contact-line"><svg width="18" height="18" viewBox="0 0 18 18"><path d="M3 1l4 1 1 4-2 1.5a10 10 0 0 0 4.5 4.5L12 10l4 1 1 4-2 2C8 17 1 10 1 3z" fill="#f7931e"/></svg>Phone:<br>+1 555-014-2870</div>
    <div class="contact-line" style="margin-top:6px"><svg width="18" height="14" viewBox="0 0 18 14"><rect x="1" y="1" width="16" height="12" fill="#f7931e"/><path d="M1 1l8 6 8-6" stroke="#1b2b49" stroke-width="1.5" fill="none"/></svg>Email:<br>hello@veltrix820.com</div>
  </div>
  <div class="footer-col" style="left:717px">
    <h5>Quick Links</h5>
    Home<br>About<br>Services<br>Blog
  </div>
  <div class="footer-col" style="left:931px">
    <h5>Other Links</h5>
    FAQ<br>Contact Us<br>Terms &amp; Conditions<br>Privacy Policy
  </div>
</footer>

</body>
</html>
```